Trucking/service truck *Updated

Cards for a trucking company. Company transfers logs to saw mills. We are looking for something edgy, modern and fun. It's very limited when it comes to trucking business card choices. Plus the owner also runs an on-site service truck. He has 20+ years mechanic experience.
Colors are open. Favorites are orange & purple, but not must have. We really want to emphasize trust, dependability and knowledge with a bright, attention getter.
On card:
Hallowell & Hallowell
Dean Hallowell - Owner/Manager/Maintenance 903-512-4097
Marla Hallowell -Office Administration/Bookkeeping 903-627-1954
4718 Juniper Ln.
Gilmer, Texas 75392
903-659-3021 - Office
Updates
Just a thought. Do you think you can combine the Taurus and Pisces signs? And put in the corner, or on the back or anything really? Thanks! You all or doing fantastic!
Industry/Entity Type
Business
Colors
Designer to choose colors to be used in the design.
Look and feel
Each slider illustrates characteristics of the customer's brand and the style your logo design should communicate.

```html
<!DOCTYPE html>
<html lang="en">
<head>
<meta charset="utf-8">
<title>Hallowell &amp; Hallowell – Business Card</title>
<link rel="stylesheet" href="https://fonts.googleapis.com/css2?family=Oswald:wght@500;600&family=Roboto:wght@400;500&display=swap">
<style>
  :root{
    --page:#e9e7e3;
    --card:#ffffff;
    --blue:#1f4fa3;
    --blue-light:#3f78d4;
    --navy:#1b2f6b;
    --red:#e8231c;
    --ink:#2a2a2a;
    --muted:#555b66;
  }
  *{margin:0;padding:0;box-sizing:border-box}
  html,body{width:1200px;height:682px;overflow:hidden;background:var(--page)}
  .card{
    position:absolute;left:100px;top:55px;width:1000px;height:572px;
    background:var(--card);overflow:hidden;
    box-shadow:0 10px 30px rgba(0,0,0,.18);
    font-family:"Roboto",Arial,sans-serif;color:var(--ink);
  }
  .card-shapes{position:absolute;inset:0}
  .brand{
    position:absolute;left:40px;top:300px;width:290px;text-align:center;
    font-family:"Roboto",Arial,sans-serif;font-weight:500;font-size:25px;color:var(--blue);
  }
  .name{
    position:absolute;left:420px;top:170px;width:300px;height:60px;
    display:flex;align-items:center;justify-content:center;
    font-family:"Oswald",Arial,sans-serif;font-weight:600;font-size:34px;
    letter-spacing:1px;color:#fff;text-transform:uppercase;
  }
  .title{
    position:absolute;left:660px;top:68px;width:310px;height:44px;
    display:flex;align-items:center;justify-content:flex-end;
    font-family:"Oswald",Arial,sans-serif;font-weight:500;font-size:22px;
    letter-spacing:2px;color:#fff;
  }
  .contact{
    position:absolute;font-size:21px;color:var(--muted);
  }
  .contact.phone-main{left:410px;top:272px}
  .contact.phone-office{left:410px;top:326px}
  .contact.email{left:690px;top:272px}
  .contact.web{left:690px;top:326px}
  .address{
    position:absolute;left:400px;top:440px;height:60px;width:580px;
    display:flex;align-items:center;
    font-size:21px;font-weight:500;color:#fff;
  }
</style>
</head>
<body>
<div class="card">
  <svg class="card-shapes" width="1000" height="572" viewBox="0 0 1000 572">
    <defs>
      <linearGradient id="topBand" x1="0" x2="1">
        <stop offset="0" stop-color="#1f4fa3"/>
        <stop offset="1" stop-color="#3f78d4"/>
      </linearGradient>
    </defs>
    <!-- top band -->
    <rect x="0" y="0" width="1000" height="30" fill="url(#topBand)"/>
    <!-- title strip -->
    <polygon points="680,68 1000,68 1000,112 660,112" fill="var(--navy)"/>
    <!-- brand mark circle -->
    <circle cx="185" cy="200" r="70" fill="var(--blue)"/>
    <!-- name block -->
    <rect x="360" y="170" width="60" height="60" fill="var(--red)"/>
    <circle cx="390" cy="191" r="9" fill="#fff"/>
    <path d="M372 220 q18 -22 36 0 z" fill="#fff"/>
    <rect x="420" y="170" width="300" height="60" fill="var(--navy)"/>
    <!-- contact icons -->
    <g fill="var(--ink)">
      <path d="M378 276 l6 -2 4 8 -3 3 q3 6 9 9 l3 -3 8 4 -2 6 q-14 2 -25 -25z"/>
      <rect x="377" y="330" width="20" height="20" fill="none" stroke="var(--ink)" stroke-width="2.5"/>
      <rect x="656" y="278" width="22" height="15"/>
      <path d="M656 278 l11 8 11 -8" stroke="#fff" stroke-width="1.5" fill="none"/>
      <circle cx="667" cy="340" r="10" fill="none" stroke="var(--ink)" stroke-width="2.5"/>
      <path d="M657 340 h20 M667 330 q-6 10 0 20 q6 -10 0 -20" stroke="var(--ink)" stroke-width="1.8" fill="none"/>
    </g>
    <!-- address band -->
    <rect x="330" y="440" width="670" height="60" fill="var(--red)"/>
    <path d="M372 484 q-12 -14 -12 -22 a12 12 0 0 1 24 0 q0 8 -12 22z" fill="#fff"/>
    <circle cx="372" cy="462" r="4" fill="var(--red)"/>
    <rect x="330" y="522" width="670" height="22" fill="var(--blue)"/>
    <!-- corner accents -->
    <rect x="220" y="500" width="60" height="72" fill="var(--blue)"/>
    <rect x="280" y="500" width="50" height="72" fill="var(--red)"/>
  </svg>

  <div class="brand">Hallowell &amp; Hallowell</div>
  <div class="title">GENERAL MANAGER</div>
  <div class="name">Dean Hallowell</div>

  <div class="contact phone-main">903-512-4097</div>
  <div class="contact phone-office">903-659-3021</div>
  <div class="contact email">dean@hallowellhauling.com</div>
  <div class="contact web">www.hallowellhauling.com</div>

  <div class="address">4718 Juniper Ln., Gilmer, Texas 75392</div>
</div>
</body>
</html>
```